Bifold for voip company

Bifold for cloud voip company

Target Market(s)

Business owners

Industry/Entity Type

Software Developer

Colors

Designer to choose colors to be used in the design.

Requirements
Must have
• Modern clean design,
• will provide content to design winner

```html
<!DOCTYPE html>
<html lang="en">
<head>
<meta charset="utf-8">
<title>Nexora – VoIP Bifold Brochure</title>
<link href="https://fonts.googleapis.com/css2?family=Black+Ops+One&family=Roboto+Condensed:wght@300;400&family=Saira+Condensed:wght@300;400&display=swap" rel="stylesheet">
<style>
  :root{
    --teal:#27d3c3;
    --teal-deep:#16a597;
    --ink:#0c0c0c;
    --panel:#141414;
    --panel-soft:#1c1c1c;
    --text-light:#e8e8e8;
    --text-muted:#a9a9a9;
    --stage:#ebebeb;
    --label:#111;
  }
  html,body{margin:0;padding:0;width:1200px;height:1200px;overflow:hidden;background:var(--stage);}
  body{position:relative;font-family:"Roboto Condensed",Arial,sans-serif;}
  .spread-label{position:absolute;left:80px;font-family:"Black Ops One",Impact,sans-serif;font-size:26px;color:var(--label);letter-spacing:1px;}
  .spread{position:absolute;left:80px;width:1040px;height:520px;background:var(--panel);box-shadow:0 6px 18px rgba(0,0,0,.25);overflow:hidden;}
  .spread svg.shapes{position:absolute;inset:0;}
  .outside{top:52px;}
  .inside{top:632px;}
  .label-outside{top:14px;}
  .label-inside{top:594px;}
  .txt{position:absolute;color:var(--text-light);}
  .slogan{font-family:"Saira Condensed",sans-serif;font-weight:300;font-size:34px;line-height:1.1;color:#fff;text-align:center;width:220px;}
  .heading{font-family:"Saira Condensed",sans-serif;font-weight:400;color:#fff;}
  .body-copy{font-size:8.5px;line-height:1.35;color:var(--text-muted);margin:0 0 6px;}
  .contact-list{position:absolute;left:296px;top:410px;list-style:none;margin:0;padding:0;}
  .contact-list li{display:flex;align-items:center;gap:8px;height:30px;font-family:"Saira Condensed",sans-serif;font-size:13px;color:var(--text-light);white-space:nowrap;}
  .contact-list svg{flex:none;}
  .brand-lockup{position:absolute;display:flex;align-items:center;gap:10px;font-family:"Roboto Condensed",sans-serif;font-weight:400;color:var(--ink);letter-spacing:3px;}
  .brand-lockup .dot{width:26px;height:26px;border-radius:50%;background:var(--ink);}
</style>
</head>
<body>

<div class="spread-label label-outside">Outside</div>
<section class="spread outside">
  <svg class="shapes" width="1040" height="520" viewBox="0 0 1040 520">
    <defs>
      <linearGradient id="cityGlow" x1="0" y1="0" x2="0" y2="1">
        <stop offset="0" stop-color="#2a2a2a"/>
        <stop offset=".55" stop-color="#4a4a4a"/>
        <stop offset="1" stop-color="#1e1e1e"/>
      </linearGradient>
    </defs>
    <rect class="photo-area" x="520" y="0" width="520" height="290" fill="url(#cityGlow)" role="img" aria-label="Night city skyline with glowing network nodes and wifi signals"/>
    <rect x="520" y="290" width="520" height="230" fill="var(--panel-soft)"/>
    <line x1="520" y1="0" x2="520" y2="520" stroke="#000" stroke-opacity=".5"/>
    <polyline points="0,200 190,310 520,290 660,380" fill="none" stroke="var(--teal)" stroke-width="7"/>
    <polygon points="0,222 190,332 520,312 660,410 660,434 520,338 192,358 0,248" fill="var(--teal)"/>
    <polyline points="860,300 1040,272" fill="none" stroke="var(--teal)" stroke-width="7"/>
    <polygon points="870,322 1040,296 1040,320 870,346" fill="var(--teal)"/>
    <polygon points="150,118 207,30 323,30 380,118 323,206 207,206" fill="var(--teal-deep)"/>
    <polygon points="160,110 217,22 333,22 390,110 333,198 217,198" fill="var(--teal)"/>
    <polygon points="590,335 665,222 815,222 890,335 815,448 665,448" fill="var(--teal)"/>
  </svg>

  <div class="txt slogan" style="left:170px;top:58px;">Voip Slogan<br>Here</div>

  <div class="txt" style="left:32px;top:340px;width:250px;">
    <div class="heading" style="font-size:26px;margin-bottom:8px;">Heading 1.53</div>
    <p class="body-copy">Lorem ipsum dolor sit amet, consectetuer adipiscing elit. Aenean commodo ligula eget dolor. Aenean massa. Cum sociis natoque penatibus et magnis dis parturient montes, nascetur ridiculus mus. Donec quam felis, ultricies nec, pretium quis, sem.</p>
    <p class="body-copy">Nulla consequat massa quis enim. Donec pede justo, fringilla vel, aliquet nec, vulputate eget, arcu. In enim justo, rhoncus ut, imperdiet a, venenatis vitae, justo.</p>
  </div>

  <ul class="contact-list">
    <li>
      <svg width="26" height="24" viewBox="0 0 26 24"><polygon points="0,12 6.5,1 19.5,1 26,12 19.5,23 6.5,23" fill="var(--teal)"/><path d="M13 5a4 4 0 0 1 4 4c0 3-4 8-4 8s-4-5-4-8a4 4 0 0 1 4-4z" fill="var(--ink)"/><circle cx="13" cy="9" r="1.5" fill="var(--teal)"/></svg>
      14 Linden Court, Suite 3
    </li>
    <li>
      <svg width="26" height="24" viewBox="0 0 26 24"><polygon points="0,12 6.5,1 19.5,1 26,12 19.5,23 6.5,23" fill="var(--teal)"/><circle cx="13" cy="12" r="6" fill="none" stroke="var(--ink)" stroke-width="1.6"/><ellipse cx="13" cy="12" rx="2.6" ry="6" fill="none" stroke="var(--ink)" stroke-width="1.2"/><line x1="7" y1="12" x2="19" y2="12" stroke="var(--ink)" stroke-width="1.2"/></svg>
      www.nexoravoice.com
    </li>
    <li>
      <svg width="26" height="24" viewBox="0 0 26 24"><polygon points="0,12 6.5,1 19.5,1 26,12 19.5,23 6.5,23" fill="var(--teal)"/><path d="M9 6l3 0 1 3-2 1.5a7 7 0 0 0 3.5 3.5L16 12l3 1 0 3c-6 1-11-4-10-10z" fill="var(--ink)"/></svg>
      0800 555 0142
    </li>
  </ul>

  <div class="brand-lockup" style="left:652px;top:318px;font-size:36px;"><span class="dot"></span>NEXORA</div>

  <div class="txt" style="left:548px;top:458px;width:470px;">
    <div class="heading" style="font-size:16px;margin-bottom:4px;">Curabitur ullamcorper ultricies nisi. Nam eget dui.</div>
    <p class="body-copy">Aenean vulputate eleifend tellus. Aenean leo ligula, porttitor eu, consequat vitae, eleifend ac, enim. Aliquam lorem ante, dapibus in, viverra quis, feugiat a, tellus.</p>
  </div>
</section>

<div class="spread-label label-inside">Inside</div>
<section class="spread inside" style="background:var(--ink);">
  <svg class="shapes" width="1040" height="520" viewBox="0 0 1040 520">
    <defs>
      <linearGradient id="earthGlow" x1="0" y1="0" x2="1" y2="1">
        <stop offset="0" stop-color="#2b2b2b"/>
        <stop offset=".6" stop-color="#555"/>
        <stop offset="1" stop-color="#8a8a8a"/>
      </linearGradient>
      <radialGradient id="globeGlow" cx=".5" cy=".5" r=".6">
        <stop offset="0" stop-color="#d8d8d8"/>
        <stop offset="1" stop-color="#3a3a3a"/>
      </radialGradient>
    </defs>
    <polygon points="465,0 1040,0 1040,240 770,300 520,300 520,440 420,200" fill="url(#earthGlow)" role="img" aria-label="Earth from orbit with a satellite and digital data dashboards"/>
    <polygon points="420,0 465,0 420,200 520,440 520,505 375,200" fill="var(--teal)"/>
    <line x1="520" y1="0" x2="520" y2="520" stroke="#000" stroke-opacity=".5"/>
    <rect x="520" y="300" width="46" height="220" fill="var(--teal)"/>
    <g fill="none" stroke="var(--ink)" stroke-width="2">
      <path d="M531 345a6 6 0 0 1 4-10 8 8 0 0 1 15 2 5 5 0 0 1 1 8z" fill="var(--ink)"/>
      <line x1="537" y1="345" x2="537" y2="352"/><line x1="543" y1="345" x2="543" y2="352"/><line x1="549" y1="345" x2="549" y2="352"/>
      <rect x="530" y="397" width="26" height="17" rx="1" fill="var(--ink)"/>
      <line x1="543" y1="414" x2="543" y2="420"/><line x1="536" y1="421" x2="550" y2="421"/>
      <circle cx="541" cy="470" r="8"/><line x1="547" y1="476" x2="555" y2="484" stroke-width="3"/>
    </g>
    <polygon points="770,345 836,240 974,240 1040,345 974,450 836,450" fill="var(--ink)"/>
    <polygon points="782,345 842,250 968,250 1028,345 968,440 842,440" fill="var(--teal)"/>
    <polygon points="40,330 75,270 145,270 180,330 145,390 75,390" fill="var(--teal)"/>
    <polygon points="52,330 82,280 138,280 168,330 138,380 82,380" fill="url(#globeGlow)" role="img" aria-label="VoIP globe emblem"/>
    <polygon points="180,250 215,190 285,190 320,250 285,310 215,310" fill="var(--teal)"/>
    <polygon points="192,250 222,200 278,200 308,250 278,300 222,300" fill="url(#globeGlow)" role="img" aria-label="Hand holding a glowing connected globe"/>
  </svg>

  <div class="txt" style="left:36px;top:30px;width:230px;">
    <div class="heading" style="font-size:16px;margin-bottom:5px;">Ipsu sit amet, conuer elit.</div>
    <p class="body-copy">Lorem ipsum dolor sit amet, consectetuer adipiscing elit. Aenean commodo ligula eget dolor. Aenean massa. Cum sociis natoque penatibus et magnis dis parturient montes, nascetur ridiculus mus. Donec quam felis, ultricies nec.</p>
  </div>

  <div class="txt" style="left:200px;top:398px;width:220px;">
    <div class="heading" style="font-size:15px;margin-bottom:5px;">Ipsu sit amet, conuer adipiscing elit.</div>
    <p class="body-copy">Lorem ipsum dolor sit amet, consectetuer adipiscing elit. Aenean massa. Cum sociis natoque penatibus et magnis dis parturient montes. Donec pede justo, fringilla vel, aliquet nec, vulputate eget, arcu.</p>
  </div>

  <div class="brand-lockup" style="left:840px;top:330px;font-size:30px;"><span class="dot" style="width:22px;height:22px;"></span>NEXORA</div>

  <div class="txt" style="left:582px;top:312px;width:185px;">
    <div class="heading" style="font-size:12.5px;margin-bottom:3px;">Lorem ipsum dolor sit amet, consectetuer adipiscing elit.</div>
    <p class="body-copy">Aenean commodo ligula eget dolor. Cum sociis natoque penatibus et magnis dis parturient montes, nascetur ridiculus mus.</p>
  </div>
  <div class="txt" style="left:582px;top:388px;width:185px;">
    <div class="heading" style="font-size:12.5px;margin-bottom:3px;">Lorem ipsum dolor sit amet, consectetuer elit.</div>
    <p class="body-copy">Nulla consequat massa quis enim. Donec pede justo, fringilla vel, aliquet nec, vulputate eget.</p>
  </div>
  <div class="txt" style="left:582px;top:456px;width:420px;">
    <div class="heading" style="font-size:12.5px;margin-bottom:3px;">Ipsum dolor sit amet, consectetuer adipiscing elit.</div>
    <p class="body-copy">Lorem ipsum dolor sit amet, consectetuer adipiscing elit. Aenean commodo ligula eget dolor. In enim justo, rhoncus ut, imperdiet a, venenatis vitae, justo. Nullam dictum felis eu pede mollis pretium.</p>
  </div>
</section>

</body>
</html>
```